Nine Moons Brochure Design Project

I need a brochure for my new company "Nine Moons". You can read all about the company at http://www.ninemoons-example.com.sg
On the website you will also get an idea of the concept of the product, as well as design. This design actually comes from a Wordpress theme.
The brochure needs to be like a print version of the website but much more summarised, high-level. I'd like to distribute it to expecting mothers at various locations such as pre-natal yoga classes. The intention is to create enough interest so these moms-to-be will surf to my website and check out what it's all about.
Target Market(s)
Expecting moms and dads (pregnant)
Industry/Entity Type
It Company
Look and feel

```html
<!DOCTYPE html>
<html lang="en">
<head>
<meta charset="utf-8">
<title>Nine Moons Brochure</title>
<link rel="stylesheet" href="https://fonts.googleapis.com/css2?family=Bebas+Neue&display=swap">
<style>
  :root {
    --page-bg: #ececec;
    --teal-deep: #6ccad2;
    --teal-soft: #acdce1;
    --paper: #ffffff;
    --headline-grey: #9ea6ad;
    --brand-grey: #4a4d50;
    --ribbon-main: #8ed5dc;
    --ribbon-tail: #7ccbd3;
    --ribbon-fold: #3f9ea7;
    --photo-light: #f7f3ef;
    --photo-warm: #e8d6c6;
  }
  * { margin: 0; padding: 0; box-sizing: border-box; }
  html, body {
    width: 1200px;
    height: 880px;
    overflow: hidden;
    background: var(--page-bg);
  }
  .brochure {
    position: absolute;
    left: 78px;
    top: 72px;
    width: 1044px;
    height: 736px;
    display: flex;
    box-shadow: 0 4px 14px rgba(0, 0, 0, 0.18);
  }
  .panel-back {
    width: 522px;
    height: 100%;
    background: linear-gradient(to right, var(--teal-deep), var(--teal-soft));
  }
  .panel-front {
    position: relative;
    width: 522px;
    height: 100%;
    background: var(--paper);
    overflow: hidden;
  }
  .cover-photo {
    position: absolute;
    left: 56px;
    top: 30px;
    width: 236px;
    height: 592px;
    background: radial-gradient(ellipse at 55% 55%, var(--photo-warm) 0%, var(--photo-light) 60%, var(--paper) 100%);
  }
  .tagline {
    position: absolute;
    left: 300px;
    top: 136px;
    width: 176px;
    text-align: center;
    font-family: "Bebas Neue", sans-serif;
    color: var(--headline-grey);
    font-size: 21px;
    line-height: 32px;
    letter-spacing: 0;
    white-space: nowrap;
  }
  .tagline-lead {
    display: block;
    font-size: 34px;
    line-height: 40px;
    letter-spacing: 2px;
  }
  .brand-name {
    position: absolute;
    left: 335px;
    top: 566px;
    font-family: "Bebas Neue", sans-serif;
    font-size: 26px;
    letter-spacing: 1px;
    color: var(--brand-grey);
  }
  .ribbon {
    position: absolute;
    left: 38px;
    top: 623px;
    width: 444px;
    height: 62px;
  }
  .ribbon svg { display: block; }
  .ribbon-text {
    position: absolute;
    left: 40px;
    top: 0;
    width: 364px;
    height: 44px;
    display: flex;
    align-items: center;
    justify-content: center;
    font-family: "Bebas Neue", sans-serif;
    font-size: 17px;
    letter-spacing: 0.6px;
    color: var(--paper);
    white-space: nowrap;
  }
</style>
</head>
<body>
  <div class="brochure">
    <section class="panel-back"></section>
    <section class="panel-front">
      <div class="cover-photo" role="img" aria-label="Photograph of an expecting mother in white, gently holding her belly"></div>
      <p class="tagline">
        <span class="tagline-lead">...Relax...</span>
        And let us take<br>
        care of planning,<br>
        organising and<br>
        preparing for the<br>
        arrival of your<br>
        little one!
      </p>
      <div class="brand-name">Nine Moons</div>
      <div class="ribbon">
        <svg width="444" height="62" viewBox="0 0 444 62" aria-hidden="true">
          <polygon points="0,16 66,16 66,56 0,56 18,36" fill="var(--ribbon-tail)"/>
          <polygon points="444,16 378,16 378,56 444,56 426,36" fill="var(--ribbon-tail)"/>
          <polygon points="40,44 66,56 66,44" fill="var(--ribbon-fold)"/>
          <polygon points="404,44 378,56 378,44" fill="var(--ribbon-fold)"/>
          <rect x="40" y="0" width="364" height="44" fill="var(--ribbon-main)"/>
          <rect x="44" y="4" width="356" height="36" fill="none" stroke="#ffffff" stroke-opacity="0.7" stroke-width="1" stroke-dasharray="3 3"/>
        </svg>
        <div class="ribbon-text">Personalised Baby Planner &amp; Maternity Concierge</div>
      </div>
    </section>
  </div>
</body>
</html>
```